artist "stamp" design

Im a young artist. I`m making a stamp with my information so i can make homemade business cards, so I need the following information to look good together and simple to read:

Lorena Batalla Quiroga

www.lorebtqz.com

lorenabq47@fotmail.example

i want a very clan look, but with some personality. a simple logo or "look" would be great but nothing to fancy.

An idea I had was to make it look like it was written with a typewriter or a concept like that...be creative! thank you!
Updates

I don't want any image or icon, just letters, I need it to be compacto, I'm making a stamp

I don't want it to say photography 

I dont want my name to take over so it should stay close to the size as the rest of the info.

all my info should be included, this is not a logo its a design for a stamp meant to fin in a business card.

Target Market(s)

I'm a photographer, I want something very simple and I need this to make a stamp that ill use to pit on my cards and CV. I want something simple and modern

Industry/Entity Type

Business

Logo Text

Lorena Batalla Quiroga

Logo styles of interest
Abstract Logo
Wordmark Logo
Lettermark Logo
Font styles to use
Serif
Sans Serif

Requirements
Must have
• Has to look young and fresh
Nice to have
• Have to see how it looks on a business card with website and and email
Should not have
• Images

```html
<!DOCTYPE html>
<html lang="en">
<head>
<meta charset="utf-8">
<title>Lorena Batalla Quiroga — Stamp</title>
<link rel="stylesheet" href="https://fonts.googleapis.com/css2?family=Courier+Prime&family=Montserrat:wght@700&display=swap">
<style>
  :root {
    --paper: #ffffff;
    --ink: #000000;
    --ink-reverse: #ffffff;
  }
  html, body {
    margin: 0;
    padding: 0;
    width: 1200px;
    height: 1000px;
    overflow: hidden;
    background: var(--paper);
  }
  .canvas {
    width: 1200px;
    height: 1000px;
    display: flex;
    align-items: center;
    justify-content: center;
  }
  .stamp {
    width: 720px;
    height: auto;
    display: block;
  }
  .stamp .band {
    fill: var(--paper);
    stroke: var(--ink);
    stroke-width: 1.6;
    stroke-linejoin: round;
  }
  .stamp .marker {
    fill: var(--ink);
  }
  .stamp .info {
    font-family: "Courier Prime", "Courier New", monospace;
    font-size: 17px;
    fill: var(--ink);
    text-anchor: middle;
    dominant-baseline: central;
  }
  .stamp .marker-letter {
    font-family: "Montserrat", Arial, sans-serif;
    font-weight: 700;
    font-size: 14px;
    fill: var(--ink-reverse);
    text-anchor: middle;
    dominant-baseline: central;
  }
</style>
</head>
<body>
  <main class="canvas">
    <svg class="stamp" viewBox="0 0 452 169" xmlns="http://www.w3.org/2000/svg" aria-label="Contact stamp for Lorena Batalla Quiroga">
      <!-- name band -->
      <polygon class="band band-name" points="1,1 419,1 450,56 32,56"/>
      <text class="info info-name" x="214" y="28">Lorena Batalla Quiroga</text>

      <!-- web band -->
      <polygon class="band band-web" points="32,56 450,56 419,112 1,112"/>
      <polygon class="marker marker-web" points="32,56 64,112 1,112"/>
      <text class="marker-letter" x="32" y="93">W</text>
      <text class="info info-web" x="214" y="86">www.lorebtqz.com</text>

      <!-- email band -->
      <polygon class="band band-email" points="1,112 419,112 450,167 32,167"/>
      <polygon class="marker marker-email" points="418,112 451,167 386,167"/>
      <text class="marker-letter" x="418" y="148">E</text>
      <text class="info info-email" x="210" y="139">lorenabq47@fotmail.example</text>
    </svg>
  </main>
</body>
</html>
```